GHollis Busisness Card

I am an aerospace consultant and at this time only need business cards.

Industry/Entity Type

Business

Contact Information for Business Card

Hollis Partners,LLC
Gerald T. Hollis

348 Birch Hollow Road
Madison AL 35762

256-555-0148 (cell)
256-555-0173 (fax)

geraldhollis@mailbrook.net

```html
<!DOCTYPE html>
<html lang="en">
<head>
<meta charset="utf-8">
<title>Hollis Partners, LLC – Business Card</title>
<link rel="stylesheet" href="https://fonts.googleapis.com/css2?family=Open+Sans:wght@400;700&display=swap">
<style>
  :root {
    --backdrop: #d9dadc;
    --card-black: #000000;
    --accent-blue: #0077c2;
    --name-blue: #1a7cc4;
    --title-cream: #fffbea;
    --text-white: #ffffff;
    --icon-blue: #1a7cc4;
  }
  * { margin: 0; padding: 0; box-sizing: border-box; }
  html, body {
    width: 1200px;
    height: 1200px;
    overflow: hidden;
    background: var(--backdrop);
    font-family: "Open Sans", Verdana, sans-serif;
  }
  .business-card {
    position: absolute;
    left: 152px;
    top: 342px;
    width: 902px;
    height: 514px;
    background: var(--card-black);
    overflow: hidden;
  }
  .accent-band {
    position: absolute;
    left: 0;
    top: 214px;
    width: 902px;
    height: 18px;
    background: linear-gradient(90deg, rgba(0,119,194,0.25) 0%, var(--accent-blue) 55%, var(--accent-blue) 100%);
  }
  .company-name {
    position: absolute;
    left: 58px;
    top: 78px;
    font-size: 56px;
    line-height: 72px;
    font-weight: 700;
    color: var(--title-cream);
    letter-spacing: 0.5px;
    white-space: nowrap;
  }
  .person {
    position: absolute;
    left: 80px;
    top: 308px;
    width: 320px;
    text-align: center;
  }
  .person-name {
    font-size: 27px;
    font-weight: 700;
    color: var(--name-blue);
    line-height: 34px;
    letter-spacing: 0.5px;
  }
  .person-role {
    font-size: 22px;
    color: var(--text-white);
    line-height: 30px;
    letter-spacing: 0.3px;
  }
  .contact-list {
    position: absolute;
    left: 478px;
    top: 311px;
    list-style: none;
    color: var(--text-white);
    font-size: 24px;
    letter-spacing: 0.4px;
  }
  .contact-item {
    display: flex;
    align-items: flex-start;
    line-height: 32px;
  }
  .contact-item.phone { margin-top: 14px; }
  .contact-item.fax { margin-top: 1px; }
  .contact-item.email { margin-top: 9px; }
  .contact-icon {
    width: 24px;
    height: 24px;
    flex: none;
    margin: 4px 13px 0 0;
  }
</style>
</head>
<body>
  <section class="business-card">
    <div class="accent-band" role="img" aria-label="Decorative blue accent band across the card"></div>

    <h1 class="company-name">Hollis Partners,LLC</h1>

    <div class="person">
      <p class="person-name">Gerald T. Hollis</p>
      <p class="person-role">Aerospace consultant</p>
    </div>

    <ul class="contact-list">
      <li class="contact-item address">
        <svg class="contact-icon" viewBox="0 0 24 24" aria-hidden="true">
          <circle cx="12" cy="12" r="11" fill="var(--text-white)"/>
          <path d="M5 12 L12 6 L19 12 H17 V18 H7 V12 Z" fill="var(--icon-blue)"/>
          <rect x="10.5" y="14" width="3" height="4" fill="var(--text-white)"/>
        </svg>
        <span>348 Birch Hollow Road<br>Madison AL 35762</span>
      </li>
      <li class="contact-item phone">
        <svg class="contact-icon" viewBox="0 0 24 24" aria-hidden="true">
          <circle cx="12" cy="12" r="11" fill="var(--text-white)"/>
          <path d="M8 6 L10.5 9 L9 10.5 C10 12.5 11.5 14 13.5 15 L15 13.5 L18 16 L16 18.5 C11 18 6 13 5.5 8 Z" fill="var(--icon-blue)"/>
        </svg>
        <span>256-555-0148</span>
      </li>
      <li class="contact-item fax">
        <svg class="contact-icon" viewBox="0 0 24 24" aria-hidden="true">
          <circle cx="12" cy="12" r="11" fill="var(--text-white)"/>
          <rect x="8" y="5" width="8" height="5" fill="var(--icon-blue)"/>
          <rect x="5" y="10" width="14" height="6" rx="1" fill="var(--icon-blue)"/>
          <rect x="8" y="14" width="8" height="5" fill="var(--text-white)" stroke="var(--icon-blue)" stroke-width="1.2"/>
        </svg>
        <span>256-555-0173</span>
      </li>
      <li class="contact-item email">
        <svg class="contact-icon" viewBox="0 0 24 24" aria-hidden="true">
          <circle cx="12" cy="12" r="11" fill="var(--text-white)"/>
          <rect x="5" y="7.5" width="14" height="9" fill="var(--icon-blue)"/>
          <path d="M5 7.5 L12 13 L19 7.5" fill="none" stroke="var(--text-white)" stroke-width="1.3"/>
        </svg>
        <span>geraldhollis@mailbrook.net</span>
      </li>
    </ul>
  </section>
</body>
</html>
```